Health and Wellness company needs flyer to promote free seminar

Stride reform studio is a health and wellness company that offers an exercise program designed by physical therapists to help relieve pain and improve mobility. Our business is a new concept that is not well understood by the public. In order to promote our business we offer a free seminar where we present information regarding the underlying cause of pain and tightness. During the seminar we also perform a posture screen and movement testing for all participants.

Target Market(s)

Mostly healthy and active women ages 25-65

Industry/Entity Type

Health And Wellness

Font styles to use
Sans Serif

Colors

Designer to choose colors to be used in the design.

Requirements
Must have
• Title: Eliminate Pain and Tightness For Good
• Paragraph: Stride Reform Studio offers a free 60 minute seminar: "The Busy Walker's Handbook to Bending and Standing Taller."
• What to Expect:
• • Identify the underlying cause of your pain and mobility issues
• • Expose what gets in the way of you moving and feeling better
• • Learn why traditional exercises don’t help and can actually make the problem worse
• • Reveal what your posture is saying and how that impacts you
• • Experience your muscle imbalances through movement tests
• • Discover the training method that realigns your posture, increases your mobility and reduces your pain
• Call to action: RSVP online at stridereformstudio.com
Nice to have
• Use a relevant image showing a female dealing with tightness in the low back, legs, etc.
• Emphasize that the seminar is FREE.
• Make the call to action prominent.

```html
<!DOCTYPE html>
<html lang="en">
<head>
<meta charset="utf-8">
<title>Stride Reform Studio – Free 60 Minute Seminar</title>
<link rel="stylesheet" href="https://fonts.googleapis.com/css2?family=Open+Sans:wght@300;400;600;700&family=Oxygen:wght@400;700&display=swap">
<style>
  :root {
    --purple: #5a5ca8;
    --orange: #f39322;
    --orange-light: #f7a33a;
    --white: #ffffff;
    --ink: #1f1f1f;
    --gray-light: #e9eaec;
    --gray-mid: #b9bcc1;
    --skin: #d8b6a2;
    --skin-deep: #b98c74;
    --shirt-gray: #6e7177;
  }
  * { margin: 0; padding: 0; box-sizing: border-box; }
  html, body { width: 879px; height: 1200px; overflow: hidden; background: var(--white); }
  .flyer {
    position: relative;
    width: 879px;
    height: 1200px;
    overflow: hidden;
    font-family: "Open Sans", Arial, sans-serif;
    color: var(--white);
    background: var(--white);
  }
  .shapes { position: absolute; inset: 0; }

  .brand {
    position: absolute;
    left: 26px; top: 20px;
    display: flex; align-items: center; gap: 16px;
  }
  .brand-mark { width: 82px; height: 82px; background: var(--orange); }
  .brand-name {
    font-family: "Oxygen", Arial, sans-serif;
    font-weight: 700;
    font-size: 40px;
    color: var(--purple);
    letter-spacing: -0.5px;
  }

  .banner-text {
    font-family: "Oxygen", Arial, sans-serif;
    font-weight: 700;
    font-size: 42px;
    fill: var(--white);
  }

  .offer { position: absolute; left: 28px; top: 324px; line-height: 1; }
  .offer-free { font-weight: 700; font-size: 70px; display: block; }
  .offer-length { font-weight: 300; font-size: 70px; display: block; margin-top: 4px; }
  .offer-kind { font-weight: 700; font-size: 56px; display: block; margin-top: 2px; }

  .expect { position: absolute; left: 30px; top: 566px; width: 680px; }
  .expect-title { font-weight: 300; font-size: 34px; margin-bottom: 20px; }
  .expect-list { list-style: none; }
  .expect-list li {
    position: relative;
    padding-left: 26px;
    font-size: 14.5px;
    line-height: 22px;
    margin-bottom: 16px;
    white-space: nowrap;
  }
  .expect-list li::before {
    content: "";
    position: absolute; left: 4px; top: 5px;
    width: 6px; height: 11px;
    border-right: 2px solid var(--orange-light);
    border-bottom: 2px solid var(--orange-light);
    transform: rotate(40deg);
  }
  .expect-list strong { font-weight: 600; text-decoration: underline; text-underline-offset: 3px; }

  .quote-mark {
    position: absolute; left: 12px; top: 980px;
    font-family: "Oxygen", Arial, sans-serif;
    font-weight: 700; font-size: 150px; line-height: 1;
    color: var(--orange-light);
    filter: brightness(1.15);
  }
  .guide-title {
    position: absolute; left: 42px; top: 1032px;
    font-size: 22px; line-height: 38px; font-weight: 400;
  }
  .guide-title span { display: block; }
  .guide-title span:first-child { padding-left: 18px; }

  .rsvp {
    position: absolute; left: 36px; top: 1139px;
    display: flex; align-items: center; gap: 10px;
    font-size: 16px; color: var(--ink);
  }
  .rsvp strong { font-weight: 700; letter-spacing: 0.3px; }
</style>
</head>
<body>
<div class="flyer">
  <svg class="shapes" width="879" height="1200" viewBox="0 0 879 1200">
    <defs>
      <linearGradient id="heroFade" x1="0" y1="0" x2="1" y2="0">
        <stop offset="0" stop-color="var(--white)"/>
        <stop offset="0.22" stop-color="#f1e6e0"/>
        <stop offset="0.5" stop-color="var(--skin)"/>
        <stop offset="0.78" stop-color="var(--shirt-gray)"/>
        <stop offset="1" stop-color="#8c9097"/>
      </linearGradient>
      <radialGradient id="heroWarm" cx="0.55" cy="0.45" r="0.35">
        <stop offset="0" stop-color="var(--skin-deep)" stop-opacity="0.7"/>
        <stop offset="1" stop-color="var(--skin-deep)" stop-opacity="0"/>
      </radialGradient>
      <linearGradient id="anatomyTone" x1="0" y1="0" x2="0" y2="1">
        <stop offset="0" stop-color="var(--gray-light)"/>
        <stop offset="1" stop-color="var(--gray-mid)"/>
      </linearGradient>
      <radialGradient id="spineGlow" cx="0.5" cy="0.5" r="0.5">
        <stop offset="0" stop-color="var(--orange)" stop-opacity="0.55"/>
        <stop offset="1" stop-color="var(--orange)" stop-opacity="0"/>
      </radialGradient>
    </defs>

    <g role="img" aria-label="Physical therapist gently stretching a relaxed woman's neck and shoulder">
      <rect x="0" y="0" width="879" height="620" fill="url(#heroFade)"/>
      <rect x="0" y="0" width="879" height="620" fill="url(#heroWarm)"/>
    </g>
    <g role="img" aria-label="Grey human skeleton illustration with the lower spine highlighted in orange">
      <polygon points="700,520 879,420 879,1200 560,1200" fill="url(#anatomyTone)"/>
      <ellipse cx="790" cy="1060" rx="80" ry="110" fill="url(#spineGlow)"/>
    </g>

    <polygon class="panel-purple" points="0,172 720,560 610,1000 0,925" fill="var(--purple)"/>
    <polygon class="panel-orange" points="0,925 612,1002 560,1200 0,1200" fill="var(--orange)"/>

    <polygon class="headline-band" points="26,100 740,520 706,580 -8,160" fill="var(--orange)"/>
    <text class="banner-text" x="0" y="0" text-anchor="middle" dominant-baseline="central"
          transform="translate(366 340) rotate(30.5)">Eliminate Pain &amp; Tightness For Good</text>

    <polygon class="rsvp-bar" points="0,1126 432,1126 412,1182 0,1182" fill="var(--white)"/>

    <circle cx="740" cy="605" r="102" fill="var(--white)"/>
    <circle cx="740" cy="605" r="94" fill="#c98a6a" role="img" aria-label="Therapist stretching a woman's leg in a gym"/>
    <circle cx="650" cy="835" r="102" fill="var(--white)"/>
    <circle cx="650" cy="835" r="94" fill="#d9b8a4" role="img" aria-label="Woman holding a tight shoulder"/>
    <circle cx="542" cy="1058" r="102" fill="var(--white)"/>
    <circle cx="542" cy="1058" r="94" fill="#6f8fa8" role="img" aria-label="Two people jogging outdoors at sunrise"/>
  </svg>

  <div class="brand">
    <span class="brand-mark"></span>
    <span class="brand-name">stridereformstudio</span>
  </div>

  <p class="offer">
    <span class="offer-free">FREE</span>
    <span class="offer-length">60 minute</span>
    <span class="offer-kind">seminar</span>
  </p>

  <section class="expect">
    <h2 class="expect-title">What To Expect</h2>
    <ul class="expect-list">
      <li><strong>Identify</strong> the underlying cause of your pain and mobility issues</li>
      <li><strong>Expose</strong> what gets in the way of you moving and feeling better</li>
      <li><strong>Learn</strong> why traditional exercises don’t help and can actually make the problem worse</li>
      <li><strong>Reveal</strong> what your posture is saying and how that impacts you</li>
      <li><strong>Experience</strong> your muscle imbalances through movement tests</li>
      <li><strong>Discover</strong> the training method that realigns your posture, increases<br>your mobility and reduces your pain</li>
    </ul>
  </section>

  <div class="quote-mark">“</div>
  <p class="guide-title">
    <span>The Busy Walker's Handbook to</span>
    <span>Bending and Standing Taller.</span>
  </p>

  <p class="rsvp">
    <svg width="20" height="20" viewBox="0 0 20 20" aria-hidden="true">
      <circle cx="10" cy="10" r="9" fill="var(--ink)"/>
      <path d="M10 1v18M1 10h18M4 5q6 3 12 0M4 15q6-3 12 0M10 1q-5 9 0 18M10 1q5 9 0 18" stroke="var(--white)" stroke-width="1" fill="none"/>
    </svg>
    <span><strong>RSVP ONLINE</strong>&nbsp; at stridereformstudio.com</span>
  </p>
</div>
</body>
</html>
```